Disruptive Wine Company Business Card

We need a SINGLE-SIDED business card for a wine company that is going to destroy the wine industry as you know it.

The business is meant to be fun, easy, approachable & high tech.

Although the logo is purple & yellow we do not want purple/yellow (bright colored) cards. Maybe a light grey background with the logo on it. Purple or yellow lines/curves in the card design is OK, but it should not be too bright.

These cards will be given out to customers who want to retain the store information or pass the cards along to their friends.

Target Market(s)

young, hip, city dwelling wine lovers

Looking for a simple but unique design that isn't showy, but will be eye grabbing.

Requirements
Must have
• An eye catching design
Should not have
• Should not be too "showy".

```html
<!DOCTYPE html>
<html lang="en">
<head>
<meta charset="utf-8">
<title>Corkline Wine Company – Business Card</title>
<link rel="stylesheet" href="https://fonts.googleapis.com/css2?family=Open+Sans:wght@400;600&display=swap">
<style>
  :root {
    --backdrop: #3b3b3b;
    --card-grey: #9c9ea1;
    --card-grey-light: #a5a7aa;
    --plum: #8e3a86;
    --amber: #e0a21f;
    --ink: #464849;
    --divider: #d7d8da;
  }
  * { box-sizing: border-box; margin: 0; padding: 0; }
  html, body {
    width: 1200px; height: 820px; overflow: hidden;
    background: var(--backdrop);
    font-family: "Open Sans", Arial, sans-serif;
  }
  .stage {
    width: 1200px; height: 820px;
    display: flex; align-items: center; justify-content: center;
  }
  .business-card {
    position: relative;
    width: 900px; height: 514px;
    background: radial-gradient(ellipse at 50% 40%, var(--card-grey-light), var(--card-grey));
    overflow: hidden;
  }
  .accent-band {
    position: absolute; left: 0; right: 0; bottom: 0;
    height: 20px; background: var(--amber);
  }
  .brand {
    position: absolute; left: 60px; width: 350px; top: 150px;
    display: flex; flex-direction: column; align-items: center;
    color: var(--plum); font-weight: 400; text-align: center;
  }
  .brand-dot {
    width: 96px; height: 96px; border-radius: 50%;
    background: var(--amber); margin-bottom: 34px;
  }
  .brand-name {
    font-size: 52px; letter-spacing: 10px; line-height: 1;
    margin-right: -10px;
  }
  .brand-sub {
    font-size: 19px; letter-spacing: 6px; margin-top: 8px;
    margin-right: -6px;
  }
  .divider {
    position: absolute; left: 470px; top: 105px;
    width: 2px; height: 305px; background: var(--divider);
  }
  .contact {
    position: absolute; left: 527px; top: 98px; color: var(--ink);
  }
  .person-name {
    font-size: 31px; font-weight: 600; color: var(--plum); line-height: 1.2;
  }
  .person-role { font-size: 22px; margin-top: 6px; }
  .address { font-size: 20px; line-height: 31px; margin-top: 22px; }
  .contact-list { list-style: none; margin-top: 22px; }
  .contact-list li {
    display: flex; align-items: center; gap: 12px;
    font-size: 20px; line-height: 34px;
  }
  .contact-list svg { width: 20px; height: 20px; fill: var(--plum); flex: none; }
</style>
</head>
<body>
<main class="stage">
  <article class="business-card">
    <div class="brand">
      <span class="brand-dot"></span>
      <span class="brand-name">CORKLINE</span>
      <span class="brand-sub">WINE COMPANY</span>
    </div>

    <div class="divider"></div>

    <section class="contact">
      <h1 class="person-name">Clara Mendes</h1>
      <p class="person-role">Director</p>
      <p class="address">Suite 210 Harbor Lane<br>Portland, OR 97205, USA</p>
      <ul class="contact-list">
        <li>
          <svg viewBox="0 0 20 20" aria-hidden="true"><path d="M2 6c0-2 3-3 8-3s8 1 8 3v2h-4V6.5c-1-.4-2.5-.6-4-.6s-3 .2-4 .6V8H2z"/><path d="M4 10l2-3h8l2 3v7H4z"/></svg>
          555 210 4471
        </li>
        <li>
          <svg viewBox="0 0 20 20" aria-hidden="true"><path d="M6 1h8a1 1 0 0 1 1 1v16a1 1 0 0 1-1 1H6a1 1 0 0 1-1-1V2a1 1 0 0 1 1-1zm1 3v11h6V4zm3 12a1 1 0 1 0 0 2 1 1 0 0 0 0-2z"/></svg>
          555 318 9062
        </li>
        <li>
          <svg viewBox="0 0 20 20" aria-hidden="true"><path d="M2 5h16v10H2z" fill="none"/><path d="M2 5h16l-8 6z"/><path d="M2 6.5l8 6 8-6V15H2z"/></svg>
          hello@corkline.com
        </li>
        <li>
          <svg viewBox="0 0 20 20" aria-hidden="true"><path d="M10 2a8 8 0 1 0 0 16 8 8 0 0 0 0-16zm5.9 7h-2.5a12 12 0 0 0-1-4.6A6 6 0 0 1 15.9 9zM10 4.1c.7 1 1.3 2.8 1.4 4.9H8.6c.1-2.1.7-3.9 1.4-4.9zM7.6 4.4A12 12 0 0 0 6.6 9H4.1a6 6 0 0 1 3.5-4.6zM4.1 11h2.5a12 12 0 0 0 1 4.6A6 6 0 0 1 4.1 11zm5.9 4.9c-.7-1-1.3-2.8-1.4-4.9h2.8c-.1 2.1-.7 3.9-1.4 4.9zm2.4-.3a12 12 0 0 0 1-4.6h2.5a6 6 0 0 1-3.5 4.6z"/></svg>
          www.corkline.com
        </li>
      </ul>
    </section>

    <div class="accent-band"></div>
  </article>
</main>
</body>
</html>
```